Garden Design Flier

I would like a PDF of this half page A4 flier in soft green tones with dark green leaves.

Target Market(s)

Home owners and real estate agents

Font styles to use
Serif
Other font styles liked:
• Papyrus

Colors
acd136
9bcb3c
cadf82
fefdec

Requirements
Must have
• Green tones
Nice to have
• Leaves, vines, lawns
Should not have
• Open to ideas, but classic style

```html
<!DOCTYPE html>
<html lang="en">
<head>
<meta charset="utf-8">
<title>Kitchen Plot Gardens – Flier</title>
<link rel="stylesheet" href="https://fonts.googleapis.com/css2?family=Bodoni+Moda:wght@500&family=Lato:ital,wght@0,300;0,400;0,700;1,400&display=swap">
<style>
  :root {
    --paper: #ffffff;
    --panel: #e6eadb;
    --brown: #54453e;
    --green: #4a9468;
    --icon: #3f8a5e;
    --leaf-dark: #6f9a6a;
    --leaf-mid: #9dbf8f;
    --leaf-light: #cfe0c3;
  }
  * { margin: 0; padding: 0; box-sizing: border-box; }
  html, body { width: 1200px; height: 846px; overflow: hidden; background: var(--paper); }
  .flier { position: relative; width: 1200px; height: 846px; overflow: hidden; background: var(--paper); font-family: "Lato", sans-serif; color: var(--brown); }
  .leaf-border {
    position: absolute; inset: 0;
    background:
      radial-gradient(ellipse 260px 180px at 6% 10%, var(--leaf-mid), transparent 70%),
      radial-gradient(ellipse 300px 200px at 40% 4%, var(--leaf-dark), transparent 70%),
      radial-gradient(ellipse 260px 200px at 96% 12%, var(--leaf-dark), transparent 70%),
      radial-gradient(ellipse 200px 320px at 2% 60%, var(--leaf-mid), transparent 70%),
      radial-gradient(ellipse 200px 320px at 98% 60%, var(--leaf-mid), transparent 70%),
      radial-gradient(ellipse 320px 160px at 30% 98%, var(--leaf-dark), transparent 70%),
      radial-gradient(ellipse 320px 160px at 78% 98%, var(--leaf-mid), transparent 70%),
      var(--leaf-light);
  }
  .card {
    position: absolute; left: 87px; top: 92px; width: 1028px; height: 661px;
    background: var(--panel); box-shadow: 0 4px 10px rgba(0,0,0,0.12);
  }
  .brand { position: absolute; left: 44px; top: 38px; font-family: "Bodoni Moda", serif; font-weight: 500; font-size: 108px; line-height: 84px; letter-spacing: 2px; color: var(--brown); }
  .owner { position: absolute; left: 46px; top: 250px; font-weight: 300; font-size: 27px; letter-spacing: 1px; }
  .credential { position: absolute; left: 46px; top: 288px; font-style: italic; font-size: 16px; }
  .phone { position: absolute; left: 44px; top: 510px; font-family: "Bodoni Moda", serif; font-weight: 500; font-size: 62px; color: var(--green); letter-spacing: 1px; }
  .contact { position: absolute; left: 46px; top: 584px; font-size: 25px; line-height: 37px; }
  .intro { position: absolute; left: 608px; top: 48px; width: 400px; font-style: italic; font-size: 25px; line-height: 36.5px; }
  .services { position: absolute; left: 612px; top: 358px; list-style: none; }
  .services li { display: flex; align-items: center; height: 56.5px; font-weight: 700; font-size: 31px; letter-spacing: 1px; }
  .services svg { width: 52px; height: 42px; margin-right: 14px; fill: none; stroke: var(--icon); stroke-width: 2; stroke-linecap: round; stroke-linejoin: round; }
</style>
</head>
<body>
<main class="flier">
  <div class="leaf-border" role="img" aria-label="Watercolour tropical leaves and palm fronds framing the flier"></div>
  <section class="card">
    <h1 class="brand">KITCHEN<br>PLOT</h1>
    <p class="owner">by Daniel Marsh</p>
    <p class="credential">Certificate III. Horticulture. Coastal Trade College</p>
    <p class="phone">0400-218365</p>
    <p class="contact">dan@kitchenplotgardens.com.au<br>ABN: 51824093716</p>
    <p class="intro">All your gardening and landscaping needs from design and installation to general maintenance. Bespoke vegetable gardens and potager design created to suit your site and requirements.</p>
    <ul class="services">
      <li><svg viewBox="0 0 52 42"><circle cx="16" cy="10" r="7"/><circle cx="34" cy="10" r="7"/><path d="M16 17v12M34 17v12M6 30h40v8H6z"/></svg>DESIGN</li>
      <li><svg viewBox="0 0 52 42"><path d="M8 30h36l-4 8H12zM14 30c2-8 8-10 12-10s10 2 12 10M36 4v18M32 4h8"/></svg>INSTALL</li>
      <li><svg viewBox="0 0 52 42"><path d="M4 36h44M12 36V22M12 24c-4 0-7-3-7-6 4 0 7 2 7 6zM12 22c4 0 6-3 6-6-4 0-6 2-6 6M36 36V14M36 16c-5 0-8-3-8-7 5 0 8 3 8 7zM36 14c5 0 8-3 8-7-5 0-8 3-8 7"/></svg>GROW</li>
      <li><svg viewBox="0 0 52 42"><path d="M4 24h44v14H4zM4 31h44M12 24V10M26 24V10M40 24V10M12 14l-4-4M12 14l4-4M26 14l-4-4M26 14l4-4M40 14l-4-4M40 14l4-4"/></svg>TEND</li>
      <li><svg viewBox="0 0 52 42"><path d="M8 30h10l-2 8h-6zM21 30h10l-2 8h-6zM34 30h10l-2 8h-6zM13 30v-6M26 30v-6M39 30v-6M10 8h12l6 6M16 8V4"/></svg>ENJOY</li>
    </ul>
  </section>
</main>
</body>
</html>
```